Movie poster for short film: TINDERLOCK

We need a creative, artistic, stylized poster design for our short film TINDERLOCK. We would like to see designs with graphics and bold colors more than photographs. The photographs we are posting are more for reference- you do not have to use them in the poster! We are looking for something clean and simple. The film is a drama so please don't make it funny. The mood of the film is thoughtful and introspective. Name of film should be in all caps. Things to include in the poster:
Name of film: TINDERLOCK
Lantern Hollow Productions
Starring Marisa Kovalenko

Here is a brief plot synopsis: TINDERLOCK follows one night in the life of a rebellious young woman who breaks into a diner after hours with a can of spray paint. Her intentions change after she ends up discovering what's left of a love story.

The movie is somewhat experimental, set to music for part of it with no dialog. The whole movie takes place in an old fashioned diner.

Target Market(s)

Film festival attendees between the ages of 20-50

Industry/Entity Type

Movie

Font styles to use
Sans Serif

Requirements
Must have
• See project description above- also the film is somewhat dark in nature so please don't make it too 'happy' looking.

```html
<!DOCTYPE html>
<html lang="en">
<head>
<meta charset="utf-8">
<title>TINDERLOCK — Film Poster</title>
<link rel="stylesheet" href="https://fonts.googleapis.com/css2?family=Arimo:wght@700&family=Cormorant+SC:wght@500;600&display=swap">
<style>
  :root {
    --paper: #ffffff;
    --title-red: #ee1c1c;
    --ink: #2a2224;
    --photo-hair: #d9b27a;
    --photo-skin: #e8c2a6;
    --photo-shirt: #2c2a2e;
    --photo-red: #c8231f;
    --photo-candy: #7a8f4a;
  }
  * { margin: 0; padding: 0; box-sizing: border-box; }
  html, body {
    width: 800px;
    height: 1200px;
    overflow: hidden;
    background: var(--paper);
  }
  .poster {
    position: relative;
    width: 800px;
    height: 1200px;
    background: var(--paper);
    color: var(--ink);
    text-align: center;
  }
  .studio {
    position: absolute;
    top: 78px;
    left: 0;
    width: 100%;
    font-family: "Cormorant SC", "Times New Roman", serif;
    font-weight: 600;
    font-size: 22px;
    letter-spacing: 0.12em;
  }
  .film-title {
    position: absolute;
    top: 160px;
    left: 0;
    width: 100%;
    font-family: "Arimo", Arial, sans-serif;
    font-weight: 700;
    font-size: 82px;
    line-height: 1;
    color: var(--title-red);
    letter-spacing: 0.14em;
    text-indent: 0.14em;
  }
  .billing-label {
    position: absolute;
    top: 307px;
    left: 0;
    width: 100%;
    font-family: "Cormorant SC", "Times New Roman", serif;
    font-weight: 600;
    font-size: 19px;
    letter-spacing: 0.14em;
  }
  .lead-actor {
    position: absolute;
    top: 352px;
    left: 0;
    width: 100%;
    font-family: "Cormorant SC", "Times New Roman", serif;
    font-weight: 500;
    font-size: 42px;
    letter-spacing: 0.1em;
  }
  .key-art {
    position: absolute;
    left: 160px;
    top: 500px;
    width: 485px;
    height: 700px;
    background:
      linear-gradient(180deg,
        rgba(255,255,255,0) 0%,
        var(--photo-hair) 12%,
        var(--photo-skin) 30%,
        var(--photo-skin) 44%,
        var(--photo-red) 52%,
        var(--photo-shirt) 62%,
        var(--photo-shirt) 82%,
        var(--photo-candy) 94%,
        var(--photo-red) 100%);
    border-radius: 200px 200px 0 0;
  }
</style>
</head>
<body>
  <main class="poster">
    <p class="studio">Lantern Hollow Productions</p>
    <h1 class="film-title">TINDERLOCK</h1>
    <p class="billing-label">Starring</p>
    <p class="lead-actor">Marisa Kovalenko</p>
    <div class="key-art" role="img" aria-label="Photograph of a young woman with long blonde hair resting her folded arms on top of a red-capped gumball machine filled with colourful gumballs"></div>
  </main>
</body>
</html>
```